BRIX Whitening Sandwich Board Design

We need a poster design for Brix Whitening to fit in our Sandwich Board with dimensions 90cm high and 60cm wide. The design has to reflect the BRIX Whitening by Marvane brand as well as our dental office brand.
The Tagline should be: "Make this a summer to smile about"
Also on the ad it should have:
1. An image(supplied)
2. Image of the Brix lamp
3. Call us today for an in-office whitening appointment at 780-412 7785
4. $199
I have included a sample of a typical Brix Whitening ad. Please use this as basis for the design and add our office details(LOGO, Phone number)
You could also use the photo in the sample image as a supplied image for the ad.
Thanks

```html
<!DOCTYPE html>
<html lang="en">
<head>
<meta charset="utf-8">
<title>Brix Whitening – Sandwich Board</title>
<link rel="stylesheet" href="https://fonts.googleapis.com/css2?family=Open+Sans:wght@400;600;700;800&display=swap">
<style>
  :root {
    --lime: #8dc63f;
    --lime-dark: #6fae2a;
    --navy: #1d4f9c;
    --navy-dark: #153a78;
    --ink: #1f3f80;
    --grey: #5b5f66;
    --white: #ffffff;
    --photo-a: #e9e2dc;
    --photo-b: #b89f8e;
  }
  * { box-sizing: border-box; margin: 0; padding: 0; }
  html, body { width: 898px; height: 1200px; overflow: hidden; background: #ffffff; }
  body { font-family: "Open Sans", Arial, sans-serif; }

  .board {
    position: relative;
    width: 898px; height: 1200px;
    background: linear-gradient(160deg, var(--lime) 0%, var(--lime-dark) 100%);
  }
  .panel {
    position: absolute;
    left: 34px; top: 34px; right: 34px; height: 960px;
    background: var(--white);
    border-radius: 26px;
    overflow: hidden;
  }
  .headline {
    position: absolute;
    left: 50px; top: 80px;
    width: 290px;
    color: var(--ink);
    font-weight: 600;
    font-size: 54px;
    line-height: 66px;
    letter-spacing: -0.5px;
  }
  .hero-photo {
    position: absolute;
    left: 350px; top: 0; right: 0; height: 660px;
    background: radial-gradient(circle at 55% 40%, var(--photo-a) 0%, #d8c7b9 45%, var(--photo-b) 100%);
    border-bottom-left-radius: 300px 220px;
  }
  .price-tag {
    position: absolute;
    left: -34px; top: 560px;
    width: 330px; height: 140px;
  }
  .price-tag span {
    position: absolute;
    left: 60px; top: 22px;
    color: var(--white);
    font-weight: 700;
    font-size: 72px;
    letter-spacing: -1px;
  }
  .call-to-action {
    position: absolute;
    left: 370px; top: 690px;
    color: var(--ink);
    font-size: 32px;
    line-height: 40px;
    font-weight: 600;
  }
  .call-to-action strong { font-weight: 800; }
  .phone {
    display: block;
    margin-top: 14px;
    font-size: 54px;
    font-weight: 600;
  }
  .lamp-photo {
    position: absolute;
    left: 40px; top: 740px;
    width: 190px; height: 190px;
    border-radius: 30px;
    background: radial-gradient(circle at 50% 45%, #f4f6f8 0%, #cfd6dd 65%, #aab3bc 100%);
  }
  .product-name {
    position: absolute;
    left: 250px; top: 880px;
    color: var(--ink);
    font-weight: 600;
    font-size: 32px;
    line-height: 40px;
  }

  .clinic-box {
    position: absolute;
    left: 40px; right: 40px; top: 1024px; height: 140px;
    background: var(--white);
    border-radius: 8px;
    display: flex; flex-direction: column; align-items: center; justify-content: center;
    gap: 4px;
  }
  .clinic-name {
    display: flex; align-items: center; gap: 14px;
    color: var(--grey);
    font-size: 50px;
    font-weight: 400;
    letter-spacing: 0.5px;
  }
  .clinic-name i {
    display: block; width: 26px; height: 26px;
    background: var(--lime);
  }
  .clinic-tag {
    color: var(--grey);
    font-size: 16px;
    letter-spacing: 5px;
    text-transform: uppercase;
  }
</style>
</head>
<body>
  <main class="board">
    <section class="panel">
      <div class="hero-photo" role="img" aria-label="Photo of a smiling couple embracing"></div>

      <h1 class="headline">Make this a summer to smile about.</h1>

      <div class="price-tag">
        <svg width="330" height="140" viewBox="0 0 330 140" aria-hidden="true">
          <polygon points="0,22 330,0 330,118 0,140" fill="var(--navy)"/>
          <polygon points="0,22 34,20 34,0" fill="var(--navy-dark)"/>
        </svg>
        <span>$199</span>
      </div>

      <p class="call-to-action">
        Call us today for an <strong>in-office</strong><br>
        whitening appointment.
        <span class="phone">780 412-7785</span>
      </p>

      <div class="lamp-photo" role="img" aria-label="Photo of the Brix whitening lamp"></div>
      <p class="product-name">Marvane Brix</p>
    </section>

    <footer class="clinic-box">
      <div class="clinic-name"><i></i>brightway</div>
      <div class="clinic-tag">Family Dental</div>
    </footer>
  </main>
</body>
</html>
```